Letterbox drop flyer

We are looking for some designs for some A5 flyers back to back in colour. We would like one side aimed at attracting people for home loans and the other side car loans. We would like to have one side aimed at home loans and re-financing and the other side aimed at car loans.
Somewhere on both pages in a speech bubble or a star or something creative have (New office is located on the ground floor, 47 Kestrel Ave Marlowe) as we are looking to hit our local community
We have a special offer to go on each side. On the home loans side, $100 extra cash in the customers hand if we can't find them a better mortgage product. On the car loans side we have 3 years of free roadside assistance with every loan settled with Bright Harbour Finance.
We would like to see designs with the same colours of our logo, blue and while with a professional crisp feel to it.
We want something that is going to be creative and capture the attention of our customer when they first look at it and want to read on.
We have more information on our website regarding our services and different types of home loans and vehicle loans.
We would like it to have our contac details:
Ph: 1300 648 953
www.brightharbourfinance.com.au
Like us on facebook: www.facebook.com/brightharbourfinance
Please feel free to email me with any questions
Target Market(s)
Anyone over the age of 18 looking for a car loan or home loan
Industry/Entity Type
Loan
Look and feel

```html
<!DOCTYPE html>
<html lang="en">
<head>
<meta charset="utf-8">
<title>Bright Harbour Finance – Home Loans Flyer</title>
<link rel="stylesheet" href="https://fonts.googleapis.com/css2?family=Source+Sans+3:wght@400;600;700;800&display=swap">
<style>
  :root {
    --brand-blue: #1d5fb8;
    --deep-blue: #17479a;
    --sky-blue: #2aa7df;
    --offer-red: #b01e23;
    --bar-red: #a3181c;
    --ink: #1f1f1f;
    --navy-ink: #0f2c5c;
    --paper: #ffffff;
  }
  * { box-sizing: border-box; margin: 0; padding: 0; }
  html, body {
    width: 994px; height: 1200px; overflow: hidden;
    background: var(--paper);
    font-family: "Source Sans 3", "Myriad Pro", Arial, sans-serif;
  }
  .flyer { position: relative; width: 994px; height: 1200px; overflow: hidden; }
  .flyer-shapes { position: absolute; inset: 0; }

  .brand {
    position: absolute; top: 52px; right: 48px;
    display: flex; align-items: center; gap: 14px;
  }
  .brand-square { width: 34px; height: 34px; background: var(--sky-blue); }
  .brand-name { font-size: 42px; font-weight: 700; color: var(--brand-blue); letter-spacing: 0.5px; }

  .offer {
    position: absolute; left: 40px; top: 818px; width: 500px;
    text-align: center; color: var(--ink);
  }
  .offer-amount { font-size: 76px; font-weight: 800; color: var(--offer-red); line-height: 1; }
  .offer-text { font-size: 29px; font-weight: 700; line-height: 1.12; margin-top: 4px; }

  .office {
    position: absolute; left: 560px; top: 850px; width: 400px;
    text-align: center; color: var(--navy-ink);
  }
  .office-title { font-size: 50px; font-weight: 800; color: var(--paper); line-height: 1; }
  .office-lead { font-size: 25px; font-weight: 600; margin-top: 6px; }
  .office-line { font-size: 32px; font-weight: 600; line-height: 1.2; }

  .call-bar {
    position: absolute; left: 40px; top: 1068px; width: 490px; height: 56px;
    background: var(--bar-red); color: var(--paper);
    font-size: 36px; font-weight: 700; line-height: 56px; padding-left: 22px;
  }
  .contact-list { position: absolute; left: 44px; top: 1134px; list-style: none; }
  .contact-item {
    display: flex; align-items: center; gap: 10px;
    font-size: 25px; font-weight: 600; color: var(--ink); line-height: 30px;
  }
  .icon-dot { width: 18px; height: 18px; border-radius: 50%; background: var(--sky-blue); }
  .icon-square { width: 18px; height: 18px; background: var(--brand-blue); }
</style>
</head>
<body>
<main class="flyer">
  <svg class="flyer-shapes" width="994" height="1200" viewBox="0 0 994 1200">
    <defs>
      <linearGradient id="greyFade" x1="0" y1="0" x2="1" y2="1">
        <stop offset="0" stop-color="#ffffff"/>
        <stop offset="0.45" stop-color="#eceef0"/>
        <stop offset="1" stop-color="#b9bdc2"/>
      </linearGradient>
      <linearGradient id="photoTones" x1="0" y1="0" x2="1" y2="1">
        <stop offset="0" stop-color="#c9cfc4"/>
        <stop offset="0.45" stop-color="#8ba36c"/>
        <stop offset="1" stop-color="#6f8fb8"/>
      </linearGradient>
    </defs>
    <polygon class="band-blue" points="0,270 540,175 994,175 994,720 0,820" fill="#1d5fb8"/>
    <polygon class="band-deep" points="0,520 330,820 0,820" fill="#17479a"/>
    <polygon class="band-deep" points="994,430 994,720 760,720" fill="#17479a"/>
    <polygon points="0,440 160,380 175,410 0,480" fill="#ffffff"/>
    <polygon points="700,820 994,600 994,640 760,820" fill="#ffffff"/>
    <rect x="100" y="240" width="130" height="130" fill="#2aa7df" transform="rotate(24 165 305)"/>
    <polygon role="img" aria-label="Photo of a smiling family of four standing in front of their home"
      points="165,300 560,140 620,210 660,185 880,420 470,875 410,800 360,840"
      fill="url(#photoTones)" stroke="#ffffff" stroke-width="10" stroke-linejoin="miter"/>
    <polygon points="0,820 994,715 994,1200 0,1200" fill="url(#greyFade)"/>
    <polygon points="0,812 994,707 994,717 0,822" fill="#ffffff"/>
    <polygon points="540,935 770,705 1000,935 770,1165" fill="#2aa7df"/>
  </svg>

  <header class="brand">
    <span class="brand-square"></span>
    <span class="brand-name">Bright Harbour Finance</span>
  </header>

  <section class="offer">
    <p class="offer-amount">$100</p>
    <p class="offer-text">extra cash<br>in the customers hand<br>if we can't find them<br>a better mortgage<br>product.</p>
  </section>

  <section class="office">
    <h2 class="office-title">NEW OFFICE</h2>
    <p class="office-lead">is located on the</p>
    <p class="office-line">Ground Floor,</p>
    <p class="office-line">47 Kestrel Ave Marlowe</p>
  </section>

  <p class="call-bar">CALL - 1300 648 953</p>

  <ul class="contact-list">
    <li class="contact-item"><span class="icon-dot"></span>www.brightharbourfinance.com.au</li>
    <li class="contact-item"><span class="icon-square"></span>www.facebook.com/brightharbourfinance</li>
  </ul>
</main>
</body>
</html>
```